Web App Design Project

Need to provide graphical design of 2 web pages according to attached wireframes.

Colors should be adjusted for the 65+ population meaning not too bright.

App logo should be created as well - logo should represent long and good life.

Target Market(s)

65 years old and above

```html
<!DOCTYPE html>
<html lang="en">
<head>
<meta charset="utf-8">
<title>AppName – Medications</title>
<link href="https://fonts.googleapis.com/css2?family=Arimo:wght@400;700&display=swap" rel="stylesheet">
<style>
:root{
  --page-bg:#ebebeb;
  --header-top:#62c6f2;
  --header-bottom:#3e9ad6;
  --header-line:#7fcff3;
  --btn-blue:#3c8fcd;
  --panel-grey:#eeeeee;
  --white:#ffffff;
  --title-blue:#3a8fd0;
  --text-grey:#7a7a7a;
  --side-grey:#7e8290;
  --side-active:#5a5e6c;
  --green:#5cb85c;
  --green-dark:#3e9a3a;
  --mute-btn:#8e909c;
  --card-line:#b9bccb;
  --info-teal:#2aa08a;
  --nav-bg:#f3f3f3;
  --nav-rule:#c4c4c4;
  --c-home:#f07a3a;
  --c-schedule:#3a96d6;
  --c-lab:#8a4fb8;
  --c-check:#f5a234;
  --c-profile:#2aa08a;
  --c-care:#df5040;
}
*{margin:0;padding:0;box-sizing:border-box}
html,body{width:1200px;height:900px;overflow:hidden}
body{background:radial-gradient(circle at 50% 50%,#f3f3f3,var(--page-bg));font-family:"Arimo",Arial,sans-serif;position:relative}
.app{position:absolute;left:100px;top:120px;width:1000px;height:660px;background:var(--white);box-shadow:0 12px 40px rgba(0,0,0,.25)}
.abs{position:absolute}

/* header */
.header{left:0;top:0;width:1000px;height:60px;background:linear-gradient(var(--header-top),var(--header-bottom))}
.brand{left:0;top:0;width:200px;height:60px;border-right:1px solid var(--header-line);display:flex;align-items:center;padding-left:20px;gap:10px;color:var(--white)}
.brand-mark{width:34px;height:34px;border-radius:50%;background:rgba(255,255,255,.85)}
.brand-name{font-size:18px;font-weight:700;line-height:18px}
.brand-slogan{font-size:9px;font-weight:700;line-height:12px}
.welcome{left:215px;top:21px;color:var(--white);font-size:15px}
.welcome b{font-weight:700}
.text-size{left:608px;top:18px;color:var(--white);display:flex;align-items:baseline;gap:12px}
.search{left:686px;top:14px;width:163px;height:31px;border:1px solid var(--header-line);background:rgba(255,255,255,.12);color:#d8f0fc;font-size:14px;padding:8px 9px}
.search svg{position:absolute;right:8px;top:7px}
.hbtn{top:14px;height:31px;background:var(--btn-blue);border:1px solid #6cc0ee;color:var(--white);font-weight:700;font-size:16px;text-align:center;line-height:29px}

/* sidebar */
.sidebar{left:0;top:60px;width:200px;height:470px;background:var(--panel-grey)}
.side-title{left:0;top:25px;width:200px;text-align:center;color:var(--title-blue);font-size:17px;font-weight:700}
.side-item{left:10px;width:190px;height:90px;display:flex;align-items:center;gap:10px;padding-left:29px;color:var(--side-grey);font-size:16px;font-weight:700}
.side-item.active{background:var(--white);color:var(--side-active);box-shadow:0 2px 3px rgba(0,0,0,.08)}

/* toolbar & list */
.toolbar{left:200px;top:60px;width:800px;height:70px;background:var(--panel-grey);border-left:1px solid #dcdcdc}
.add-med{left:30px;top:23px;display:flex;align-items:center;gap:8px;color:var(--title-blue);font-size:16px;font-weight:700}
.gear{left:744px;top:22px}
.med{left:229px;width:742px;height:62px;border:1px solid var(--card-line);border-radius:3px;background:var(--white)}
.med.taken{border-color:var(--green)}
.status{position:absolute;left:14px;top:15px;width:100px;height:30px;border-radius:2px;color:var(--white);font-size:13px;font-weight:700;display:flex;align-items:center;justify-content:center;gap:6px}
.status.done{background:var(--green)}
.status.todo{background:var(--mute-btn)}
.med-name{position:absolute;left:147px;top:21px;font-size:16px;color:var(--text-grey)}
.dose{position:absolute;left:576px;top:21px;font-size:16px;font-weight:700;color:var(--title-blue)}
.form-icon{position:absolute;left:610px;top:20px}
.info{position:absolute;left:700px;top:20px}

/* bottom nav */
.nav{left:0;top:530px;width:1000px;height:130px;background:var(--nav-bg);border-top:3px solid var(--nav-rule);display:flex}
.nav-item{width:143px;height:127px;display:flex;flex-direction:column;align-items:center;font-size:14px;font-weight:700;text-align:center;line-height:17px;padding-top:28px}
.nav-item svg{height:34px;margin-bottom:16px}
.nav-item.two{line-height:17px}
.nav-item.two span{margin-top:-8px}
.nav-item.current{width:142px;background:linear-gradient(#6cc063,var(--green-dark));color:var(--white)}
</style>
</head>
<body>
<div class="app">

  <header class="abs header">
    <div class="abs brand">
      <span class="brand-mark"></span>
      <div><div class="brand-name">AppName</div><div class="brand-slogan">Here is your slogan</div></div>
    </div>
    <div class="abs welcome">Welcome back, <b>Arthur Bell</b></div>
    <div class="abs text-size"><span style="font-size:11px">A</span><span style="font-size:17px;font-weight:700">A</span><span style="font-size:20px;opacity:.85">A</span></div>
    <div class="abs search">Search
      <svg width="16" height="16" viewBox="0 0 16 16"><circle cx="6.5" cy="6.5" r="5" fill="none" stroke="#fff" stroke-width="2"/><path d="M10 10l5 5" stroke="#fff" stroke-width="2.4"/></svg>
    </div>
    <div class="abs hbtn" style="left:888px;width:32px">?</div>
    <div class="abs hbtn" style="left:934px;width:52px">Exit</div>
  </header>

  <aside class="abs sidebar">
    <div class="abs side-title">Medications</div>
    <div class="abs side-item active" style="top:70px">
      <svg width="33" height="32" viewBox="0 0 33 32" fill="none" stroke="#6a6e7c" stroke-width="2"><path d="M9 15a7.5 7.5 0 0 1 15 0"/><path d="M16.5 2v4M6 6l3 3M27 6l-3 3M2 15h4M27 15h4"/><path d="M1 19h31M1 24h31M1 29h31"/></svg>
      Morning</div>
    <div class="abs side-item" style="top:170px">
      <svg width="33" height="32" viewBox="0 0 33 32" fill="none" stroke="#8a8e9a" stroke-width="2"><circle cx="16.5" cy="16" r="7"/><path d="M16.5 2v4M16.5 26v4M3 16h4M26 16h4M7 6.5l3 3M26 6.5l-3 3M7 25.5l3-3M26 25.5l-3-3"/></svg>
      Noon</div>
    <div class="abs side-item" style="top:270px">
      <svg width="33" height="32" viewBox="0 0 33 32" fill="none" stroke="#8a8e9a" stroke-width="2"><path d="M10 13a6 6 0 0 1 11-3"/><path d="M15 2v3M6 5l2 2M24 5l-2 2"/><path d="M7 30a5 5 0 0 1 0-10 7 7 0 0 1 13-2 5 5 0 0 1 6 4 4 4 0 0 1 0 8z"/></svg>
      Afternoon</div>
    <div class="abs side-item" style="top:370px">
      <svg width="33" height="32" viewBox="0 0 33 32" fill="none" stroke="#8a8e9a" stroke-width="2"><path d="M14 2a14 14 0 1 0 16 18A12 12 0 0 1 14 2z"/></svg>
      Night</div>
  </aside>

  <div class="abs toolbar">
    <div class="abs add-med">
      <svg width="25" height="25" viewBox="0 0 25 25"><circle cx="12.5" cy="12.5" r="11.5" fill="none" stroke="#8a8e9a" stroke-width="1.6"/><path d="M12.5 6v13M6 12.5h13" stroke="#3a8fd0" stroke-width="3"/></svg>
      Add medication</div>
    <svg class="abs gear" width="26" height="26" viewBox="0 0 26 26"><circle cx="13" cy="13" r="12" fill="none" stroke="#8a8e9a" stroke-width="1.6"/><circle cx="13" cy="13" r="6" fill="none" stroke="#3a8fd0" stroke-width="3" stroke-dasharray="3 1.7"/><circle cx="13" cy="13" r="2.5" fill="#3a8fd0"/></svg>
  </div>

  <div class="abs med taken" style="top:160px">
    <div class="status done"><svg width="11" height="9" viewBox="0 0 11 9"><path d="M1 4.5l3 3L10 1" fill="none" stroke="#fff" stroke-width="2"/></svg>Taken</div>
    <div class="med-name">Velmora (indomethacin)</div>
    <div class="dose">4x</div>
    <svg class="form-icon" width="22" height="22" viewBox="0 0 22 22"><rect x="2" y="7" width="18" height="8" rx="4" transform="rotate(-45 11 11)" fill="none" stroke="#777" stroke-width="1.6"/><path d="M11 11l4.5-4.5" stroke="#777" stroke-width="5" opacity=".6"/></svg>
    <svg class="info" width="20" height="20" viewBox="0 0 20 20"><circle cx="10" cy="10" r="9" fill="none" stroke="#2aa08a" stroke-width="1.3"/><text x="10" y="14.5" font-size="12" font-style="italic" text-anchor="middle" fill="#2aa08a" font-family="Georgia,serif">i</text></svg>
  </div>

  <div class="abs med" style="top:252px">
    <div class="status todo">Mark as taken</div>
    <div class="med-name">Coravex (dabigatran)</div>
    <div class="dose">2x</div>
    <svg class="form-icon" width="22" height="22" viewBox="0 0 22 22"><rect x="2" y="4" width="11" height="16" rx="2" fill="none" stroke="#777" stroke-width="1.6"/><rect x="3.5" y="9" width="8" height="6" fill="#888"/><ellipse cx="18" cy="5" rx="2" ry="3" fill="#777"/><path d="M18 8v12" stroke="#777" stroke-width="1.8"/></svg>
    <svg class="info" width="20" height="20" viewBox="0 0 20 20"><circle cx="10" cy="10" r="9" fill="none" stroke="#2aa08a" stroke-width="1.3"/><text x="10" y="14.5" font-size="12" font-style="italic" text-anchor="middle" fill="#2aa08a" font-family="Georgia,serif">i</text></svg>
  </div>

  <div class="abs med" style="top:344px">
    <div class="status todo">Mark as taken</div>
    <div class="med-name">Gastrelle (omeprazole)</div>
    <div class="dose">1x</div>
    <svg class="form-icon" width="22" height="22" viewBox="0 0 22 22" fill="none" stroke="#777" stroke-width="1.6"><path d="M5 13l8-8 4 4-8 8z"/><path d="M15 3l4 4M17 5l3-3M5 13l4 4M2 20l4-4M8 12l1.5 1.5M10.5 9.5l1.5 1.5"/></svg>
    <svg class="info" width="20" height="20" viewBox="0 0 20 20"><circle cx="10" cy="10" r="9" fill="none" stroke="#2aa08a" stroke-width="1.3"/><text x="10" y="14.5" font-size="12" font-style="italic" text-anchor="middle" fill="#2aa08a" font-family="Georgia,serif">i</text></svg>
  </div>

  <nav class="abs nav">
    <div class="nav-item current">
      <svg width="32" height="34" viewBox="0 0 32 34"><rect x="4" y="2" width="10" height="22" rx="5" transform="rotate(-25 9 13)" fill="#fff"/><rect x="15" y="9" width="10" height="22" rx="5" transform="rotate(-60 20 20)" fill="#fff" stroke="#4fa84a" stroke-width="1.5"/></svg>
      <span>Medications</span></div>
    <div class="nav-item two" style="color:var(--c-home)">
      <svg width="16" height="34" viewBox="0 0 16 34"><rect x="5" y="1" width="6" height="24" rx="3" fill="none" stroke="#f07a3a" stroke-width="1.6"/><circle cx="8" cy="27" r="5.5" fill="#f07a3a"/><path d="M8 10v16" stroke="#f07a3a" stroke-width="2.5"/><path d="M12 6h3M12 10h3M12 14h3" stroke="#f07a3a"/></svg>
      <span>Home<br>Measurements</span></div>
    <div class="nav-item" style="color:var(--c-schedule)">
      <svg width="32" height="34" viewBox="0 0 32 34"><rect x="1.5" y="5" width="29" height="27" fill="none" stroke="#3a96d6" stroke-width="2"/><rect x="1.5" y="5" width="29" height="6" fill="#3a96d6"/><path d="M8 2v6M16 2v6M24 2v6" stroke="#3a96d6" stroke-width="2.5"/><text x="16" y="28" font-size="12" text-anchor="middle" fill="#3a96d6" font-family="Arimo,Arial,sans-serif">17</text></svg>
      <span>My Schedule</span></div>
    <div class="nav-item" style="color:var(--c-lab)">
      <svg width="34" height="34" viewBox="0 0 34 34" fill="none" stroke="#8a4fb8" stroke-width="2"><rect x="2" y="2" width="30" height="21"/><path d="M6 14h6l3-6 4 11 3-6h6"/><path d="M17 23v4M12 32l5-5 5 5"/></svg>
      <span>Lab Test Results</span></div>
    <div class="nav-item two" style="color:var(--c-check)">
      <svg width="34" height="34" viewBox="0 0 34 34" fill="#f5a234"><rect x="2" y="3" width="6" height="6" fill="none" stroke="#f5a234" stroke-width="1.6"/><rect x="2" y="14" width="6" height="6" fill="none" stroke="#f5a234" stroke-width="1.6"/><rect x="2" y="25" width="6" height="6" fill="none" stroke="#f5a234" stroke-width="1.6"/><rect x="12" y="4.5" width="20" height="3"/><rect x="12" y="15.5" width="20" height="3"/><rect x="12" y="26.5" width="20" height="3"/></svg>
      <span>Checkups &amp;<br>Procedures</span></div>
    <div class="nav-item" style="color:var(--c-profile)">
      <svg width="34" height="34" viewBox="0 0 34 34" fill="#2aa08a"><ellipse cx="17" cy="10" rx="7" ry="9"/><path d="M2 34c0-9 6-13 15-13s15 4 15 13z"/></svg>
      <span>My Profile</span></div>
    <div class="nav-item two" style="color:var(--c-care)">
      <svg width="34" height="34" viewBox="0 0 34 34"><path d="M17 31L4 18A8 8 0 0 1 17 7a8 8 0 0 1 13 11z" fill="#df5040"/></svg>
      <span>My Health Care<br>Providers</span></div>
  </nav>

</div>
</body>
</html>
```